Subway/Bus ad sign for a paid research study

We are looking for someone who can help design an effective advertisement sign for a paid research study. The ad will be displayed in subway stations/bus. The study involves fMRI and is conducted by a laboratory in the Calder Valley University.

We prefer ppt images so we could edit. Dimensions should be 46”h x 60”w, but may vary in the final version depending on our needs.

The way we would like to choose the final design is by running a pretest on plumfeed to pick the most attractive ad. Your submission would mean that you consent with this process.

Thank you for your consideration.

Target Market(s)

age 18-64, philadelphia

Requirements
Must have
• The ad must include the following information (we encourage you to come up with better/more catchy slogans)
• - We are looking for participants for a research study
• - This fMRI study is conducted by researchers at Calder Valley University
• - Email CvuCV2@lab.cvu-mail.org to see if you are eligible
• - Calder Valley University Logo
• The ad may include the following information
• - Participants get paid up to $190
Nice to have
• original attractive illustrations are highly encouraged.
Should not have
• It seems like brain photos tend to scare people away. Maybe you could focus on using survey-related images or illustrated images of the brain (vs. fMRI scans).

```html
<!DOCTYPE html>
<html lang="en">
<head>
<meta charset="utf-8">
<title>Participants Wanted – fMRI Research Study</title>
<link rel="stylesheet" href="https://fonts.googleapis.com/css2?family=Montserrat:wght@400;500;600;700;800&display=swap">
<style>
  :root {
    --red-deep: #a3262a;
    --red-warm: #b8463a;
    --red-light: #cf7a63;
    --navy: #2b3362;
    --navy-dark: #1f2752;
    --blue-bright: #16a6e6;
    --blue-mid: #1f6fb7;
    --white: #ffffff;
    --circuit-orange: #e08a2c;
  }
  * { box-sizing: border-box; margin: 0; padding: 0; }
  html, body { width: 1200px; height: 900px; overflow: hidden; background: var(--white); }
  body { font-family: "Montserrat", Arial, sans-serif; color: var(--white); }

  .sign { position: relative; width: 1200px; height: 900px; overflow: hidden; }

  /* Header band */
  .header {
    position: absolute; left: 0; top: 0; width: 1200px; height: 330px;
    background: linear-gradient(100deg, var(--red-deep) 0%, var(--red-deep) 45%, var(--red-warm) 68%, var(--red-light) 82%, var(--red-warm) 100%);
  }
  .header-frame {
    position: absolute; left: 34px; top: 36px; width: 1130px; height: 330px;
    border: 3px solid var(--navy); border-bottom: none;
  }
  .kicker {
    position: absolute; left: 356px; top: 14px; width: 488px; height: 94px;
  }
  .kicker svg { position: absolute; inset: 0; }
  .kicker-text {
    position: absolute; inset: 0; display: flex; align-items: center; justify-content: center;
    font-size: 43px; font-weight: 500; letter-spacing: 0.5px;
  }
  .headline {
    position: absolute; left: 0; top: 128px; width: 1200px; text-align: center;
    font-size: 106px; font-weight: 800; letter-spacing: 1px; line-height: 1;
    text-shadow: 0 4px 0 rgba(43, 51, 98, 0.55);
  }
  .subhead {
    position: absolute; left: 0; top: 242px; width: 1200px; text-align: center;
    font-size: 33px; font-weight: 700; letter-spacing: 0.5px;
  }
  .subhead .slashes { color: var(--navy); font-style: italic; letter-spacing: -3px; margin: 0 10px; }

  /* Offer band */
  .offer {
    position: absolute; left: 0; top: 330px; width: 1200px; height: 378px;
    background:
      radial-gradient(ellipse 420px 260px at 700px 120px, var(--blue-bright) 0%, rgba(22,166,230,0) 100%),
      linear-gradient(90deg, var(--blue-mid) 0%, var(--blue-bright) 50%, var(--blue-mid) 72%, var(--navy-dark) 100%);
  }
  .offer-visual {
    position: absolute; left: 24px; top: 0; width: 580px; height: 378px;
    background: linear-gradient(90deg, rgba(140,80,30,0.9) 0%, rgba(214,130,50,0.85) 45%, rgba(120,90,60,0.55) 80%, rgba(22,166,230,0) 100%);
  }
  .up-to { position: absolute; left: 948px; top: 80px; font-size: 21px; font-weight: 600; letter-spacing: 1px; }
  .earn {
    position: absolute; left: 640px; top: 118px; font-size: 72px; font-weight: 800;
    color: var(--navy); letter-spacing: 1px; line-height: 1;
  }
  .earn-note { position: absolute; left: 642px; top: 188px; font-size: 24px; font-weight: 500; }
  .amount {
    position: absolute; left: 872px; top: 104px; font-size: 104px; font-weight: 700;
    line-height: 1; letter-spacing: -1px;
  }
  .eligibility { position: absolute; left: 572px; top: 294px; font-size: 20px; font-weight: 700; }
  .email {
    position: absolute; left: 620px; top: 324px; font-size: 26px; font-weight: 700;
    text-decoration: underline; text-underline-offset: 4px; text-decoration-thickness: 2px;
  }
  .email-icon { position: absolute; left: 1030px; top: 290px; width: 92px; height: 64px; }

  /* Footer band */
  .footer {
    position: absolute; left: 0; top: 708px; width: 1200px; height: 192px;
    background: var(--navy);
  }
  .credit {
    position: absolute; left: 66px; top: 72px; font-size: 22px; font-weight: 500; line-height: 1.5;
  }
  .credit strong { font-weight: 700; }
  .brand {
    position: absolute; left: 830px; top: 50px; display: flex; align-items: center; gap: 16px;
  }
  .brand-mark { width: 58px; height: 58px; background: var(--white); flex: none; }
  .brand-name { font-size: 30px; font-weight: 600; line-height: 1.1; color: var(--white); width: 260px; }
</style>
</head>
<body>
<main class="sign">
  <section class="header">
    <div class="header-frame"></div>
    <div class="kicker">
      <svg viewBox="0 0 488 94" width="488" height="94" aria-hidden="true">
        <polygon points="14,0 488,0 474,94 0,94" fill="#2b3362"/>
      </svg>
      <span class="kicker-text">We are looking for</span>
    </div>
    <h1 class="headline">PARTICIPANTS</h1>
    <p class="subhead"><span class="slashes">///</span>FOR A fMRI RESEARCH STUDY<span class="slashes">///</span></p>
  </section>

  <section class="offer">
    <div class="offer-visual" role="img" aria-label="Illustration of two human head profiles overlaid with orange circuit-board lines"></div>
    <span class="up-to">UP TO</span>
    <span class="earn">EARN</span>
    <span class="earn-note">for participation</span>
    <span class="amount">$190</span>
    <p class="eligibility">To see if you are eligible, send an email to</p>
    <p class="email">CvuCV2@lab.cvu-mail.org</p>
    <svg class="email-icon" viewBox="0 0 92 64" aria-hidden="true">
      <rect x="1" y="1" width="90" height="62" rx="3" fill="#ffffff"/>
      <polyline points="4,5 46,38 88,5" fill="none" stroke="#1f5fa8" stroke-width="3"/>
      <line x1="4" y1="60" x2="36" y2="30" stroke="#1f5fa8" stroke-width="3"/>
      <line x1="88" y1="60" x2="56" y2="30" stroke="#1f5fa8" stroke-width="3"/>
    </svg>
  </section>

  <footer class="footer">
    <p class="credit">This study is conducted by researchers<br>at <strong>Calder Valley University</strong></p>
    <div class="brand">
      <span class="brand-mark"></span>
      <span class="brand-name">Calder Valley University</span>
    </div>
  </footer>
</main>
</body>
</html>
```